Modern Yoga Studio Timetable and Flyer Design

We have a comprehensive class timetable and we are wanting to a clean modern look for our Spring timetable.

We require a double sided flyer with our class timetable included.
We would prefer an A5 size (postcard) or DL (1/3 A4).

We would like the final flyer to have.
Side A : Yoga image, logo

Fennel Stretch Hall
address: 4/71 Wexcombe Lane, Pelharton
website: fennelstretch.com.au
mobile: 0471 296 814

Side B: Clear easy to read timetable with a break down of class types and website.

We would also like to have a copy of the timetable itself as a separate jpg or pdf for use on our website to download.

Thank you.
Yours kindly,
Nell

I have attached a sample of another timetable of which I like the look and feel of, however this is just a guide. I've also attached our 'new' schedule in WORD plus uploaded our last design of the front.
Updates

Target Market(s)

Women aged 30-45

Industry/Entity Type

Health And Wellness

Font styles to use
Other font styles liked:
• Brandon Grotesque, Jenna Sue

Colors
6c459b
33a6d7
ffffff

Requirements
Must have
• A definitive colour to decipher between different class types on our timetable. Where each colour represents a different class type. Colours and layouts similar to our website design, see www.fennelstretch.com.au
Nice to have
• I've included a design of another studio whose timetable design I like. One of our own yoga images instead of a stock image.
Should not have
• No dark gridlines between the cells/boxes in the timetables. Please don't use stock yoga images.

```html
<!DOCTYPE html>
<html lang="en">
<head>
<meta charset="utf-8">
<title>Fennel Stretch Hall – Spring Flyer</title>
<link rel="stylesheet" href="https://fonts.googleapis.com/css2?family=Questrial&family=Montserrat:wght@700;800&family=Pathway+Gothic+One&display=swap">
<style>
  :root{
    --violet:#6c459b;
    --violet-deep:#7a3f96;
    --violet-class:#b47cbc;
    --sky:#33a6d7;
    --sky-class:#8fcdee;
    --row-sky:#d3eaf8;
    --row-pink:#f3d6ea;
    --ink:#222;
    --frame:#3b2b4d;
    --page:#e4e4e4;
    --white:#ffffff;
    --mandala:#8a6bb3;
    --photo-a:#d9c3ac;
    --photo-b:#a98a66;
  }
  *{box-sizing:border-box;margin:0;padding:0}
  html,body{width:1200px;height:851px;overflow:hidden;background:var(--page)}
  body{position:relative;font-family:"Questrial",sans-serif;color:var(--ink)}

  /* Side A */
  .flyer-front{position:absolute;left:78px;top:123px;width:303px;height:623px;background:var(--white);overflow:hidden}
  .front-art{position:absolute;left:0;top:0}
  .brand-mark{position:absolute;left:0;top:80px;width:100%;text-align:center;font-size:21px;color:var(--sky);letter-spacing:3px;white-space:nowrap}
  .studio-title{position:absolute;left:0;top:432px;width:100%;text-align:center;font-size:29px;color:var(--violet);white-space:nowrap}
  .contact-box{position:absolute;left:17px;top:497px;width:267px;height:82px;border:3px solid var(--violet);border-bottom:none;border-radius:14px 14px 0 0;padding:9px 0 0 10px}
  .contact-phone{display:flex;align-items:center;gap:4px;font-size:32px;color:var(--violet);line-height:1;white-space:nowrap}
  .contact-address{display:flex;align-items:center;gap:7px;font-size:14px;line-height:1;margin-top:9px;padding-left:2px;white-space:nowrap}
  .web-band{position:absolute;left:0;bottom:0;width:100%;height:46px;background:var(--sky);color:var(--white);font-size:19px;text-align:center;line-height:46px;white-space:nowrap}

  /* Side B */
  .flyer-back{position:absolute;left:429px;top:291px;width:696px;height:339px;background:var(--white)}
  .timetable-title{position:absolute;left:33px;top:17px;font-family:"Montserrat",sans-serif;font-weight:800;font-size:12px;color:var(--violet-deep)}
  .timetable-frame{position:absolute;left:17px;top:35px;width:659px;border:2px solid var(--frame);border-radius:12px;overflow:hidden}
  .timetable{width:100%;border-collapse:collapse;table-layout:fixed;font-family:"Pathway Gothic One",sans-serif;font-size:13px}
  .timetable th{background:var(--violet-deep);color:var(--white);font-family:"Montserrat",sans-serif;font-size:10px;font-weight:700;height:19px;text-align:left;padding-left:14px}
  .timetable td{height:19.6px;border-right:2px solid var(--white);padding-left:8px;white-space:nowrap;color:#222}
  .timetable td:last-child{border-right:none}
  .timetable td.time{font-family:"Questrial",sans-serif;font-size:11px;padding-left:16px}
  .timetable tr:nth-child(odd) td{background:var(--row-sky)}
  .timetable tr:nth-child(even) td{background:var(--row-pink)}
  .timetable tr td.cls-sky{background:var(--sky-class)}
  .timetable tr td.cls-violet{background:var(--violet-class);color:var(--white)}
  .timetable td.center{text-align:center;padding-left:0}
  .footnote{position:absolute;left:33px;top:316px;font-size:12px}
</style>
</head>
<body>

<section class="flyer-front">
  <svg class="front-art" width="303" height="623" viewBox="0 0 303 623">
    <rect role="img" aria-label="Decorative mandala pattern" x="60" y="0" width="183" height="66" rx="6" fill="var(--mandala)" opacity="0.35"/>
    <path d="M0,150 Q150,200 303,140 L303,165 Q150,225 0,185 Z" fill="var(--sky)"/>
    <path d="M0,178 Q150,228 303,170 L303,195 Q150,250 0,205 Z" fill="var(--violet)"/>
    <path d="M0,205 Q150,250 303,195 L303,355 Q220,368 175,395 Q160,405 151,425 Q142,405 127,395 Q82,368 0,355 Z" fill="var(--sky)"/>
    <defs><linearGradient id="photoTone" x1="0" y1="0" x2="0" y2="1">
      <stop offset="0" stop-color="var(--photo-a)"/><stop offset="1" stop-color="var(--photo-b)"/></linearGradient></defs>
    <path role="img" aria-label="Photo of a yoga teacher in a side-angle stretch on a mat" d="M0,207 Q150,252 303,197 L303,345 Q220,358 175,385 Q160,395 151,413 Q142,395 127,385 Q82,358 0,345 Z" fill="url(#photoTone)"/>
  </svg>
  <div class="brand-mark">fennel stretch hall</div>
  <div class="studio-title">Fennel Stretch Hall</div>
  <div class="contact-box">
    <div class="contact-phone">
      <svg width="14" height="14" viewBox="0 0 24 24"><path d="M6.6 10.8a15 15 0 0 0 6.6 6.6l2.2-2.2c.3-.3.7-.4 1-.2 1.1.4 2.3.6 3.6.6.6 0 1 .4 1 1V20c0 .6-.4 1-1 1A17 17 0 0 1 3 4c0-.6.4-1 1-1h3.5c.6 0 1 .4 1 1 0 1.3.2 2.5.6 3.6.1.3 0 .7-.2 1z" fill="var(--violet)"/></svg>
      <span>0471 296 814</span>
    </div>
    <div class="contact-address">
      <svg width="10" height="14" viewBox="0 0 10 14"><path d="M5 0a5 5 0 0 0-5 5c0 3.5 5 9 5 9s5-5.5 5-9a5 5 0 0 0-5-5zm0 7a2 2 0 1 1 0-4 2 2 0 0 1 0 4z" fill="var(--violet)"/></svg>
      <span>4/71 Wexcombe Lane, Pelharton</span>
    </div>
  </div>
  <div class="web-band">website: fennelstretch.com.au</div>
</section>

<section class="flyer-back">
  <h1 class="timetable-title">FENNEL STRETCH SPRING TIMETABLE</h1>
  <div class="timetable-frame">
    <table class="timetable">
      <colgroup><col style="width:67px"><col style="width:83px"><col style="width:84px"><col style="width:84px"><col style="width:111px"><col style="width:79px"><col style="width:79px"><col style="width:72px"></colgroup>
      <thead><tr><th></th><th>MON</th><th>TUE</th><th>WED</th><th>THU</th><th>FRI</th><th>SAT</th><th>SUN</th></tr></thead>
      <tbody>
        <tr><td class="time">545AM</td><td></td><td class="cls-sky">RISE + SHINE*</td><td></td><td class="cls-sky">RISE + SHINE*</td><td></td><td></td><td></td></tr>
        <tr><td class="time">900AM</td><td></td><td></td><td></td><td></td><td></td><td class="cls-violet">VINYASA FLOW</td><td></td></tr>
        <tr><td class="time">915AM</td><td></td><td class="cls-sky">VINYASA FLOW</td><td></td><td></td><td></td><td></td><td class="cls-sky center">YIN</td></tr>
        <tr><td class="time">930AM</td><td class="cls-violet">SLOW FLOW</td><td></td><td></td><td class="cls-violet">VINYASA FLOW</td><td></td><td></td><td></td></tr>
        <tr><td class="time">1030AM</td><td></td><td></td><td></td><td></td><td></td><td class="cls-sky">PREGNANCY*</td><td></td></tr>
        <tr><td class="time">11AM</td><td></td><td class="cls-violet">MUM + BABY*</td><td></td><td class="cls-violet">MUM + BABY*</td><td></td><td></td><td></td></tr>
        <tr><td class="time">1215PM</td><td></td><td></td><td></td><td class="cls-sky">PREGNANCY</td><td></td><td></td><td></td></tr>
        <tr><td class="time">4PM</td><td></td><td></td><td class="cls-violet">KIDS 8-12*</td><td class="cls-violet">KIDS 5-7*</td><td></td><td class="cls-violet">VINYASA FLOW</td><td></td></tr>
        <tr><td class="time">445PM</td><td></td><td></td><td class="cls-sky">TEENS 12-16*</td><td></td><td></td><td></td><td></td></tr>
        <tr><td class="time">500PM</td><td></td><td></td><td></td><td class="cls-violet">TEENS 12 – 16*</td><td></td><td></td><td></td></tr>
        <tr><td class="time">600PM</td><td class="cls-sky">PREGNANCY*</td><td class="cls-sky">VINYASA FLOW</td><td class="cls-sky">SLOW FLOW</td><td></td><td class="cls-sky">FLOW + RESTORE</td><td></td><td></td></tr>
        <tr><td class="time">615PM</td><td></td><td></td><td></td><td class="cls-violet">PREGNANCY*</td><td></td><td></td><td></td></tr>
        <tr><td class="time">730PM</td><td class="cls-sky">VINYASA FLOW</td><td class="cls-sky">PREGNANCY*</td><td class="cls-sky">YIN + RESTORE</td><td class="cls-sky">WOMEN’S WELLNESS*</td><td></td><td></td><td></td></tr>
      </tbody>
    </table>
  </div>
  <p class="footnote">* bookings essential</p>
</section>

</body>
</html>
```